Flyer for a Payroll and Bookkeeping Companmy

Need a brochure to highlight our costs and service to hand out to clients.

Please see attachments for more information.

It Service

```html
<!DOCTYPE html>
<html lang="en">
<head>
<meta charset="utf-8">
<title>Northfield Ridge — Bookkeeping &amp; Payroll Pricing</title>
<link rel="stylesheet" href="https://fonts.googleapis.com/css2?family=Saira+Semi+Condensed:wght@300;400;700;800&family=Saira:wght@200;300;400&display=swap">
<style>
  :root{
    --orange:#e87722;
    --orange-deep:#c9621a;
    --blue:#1468b8;
    --blue-deep:#0b4f96;
    --ink:#2d2d2d;
    --muted:#8a8a8a;
    --rule:#b9bcc0;
    --stage:#3a3a3c;
    --charcoal:#3b3b3d;
    --white:#ffffff;
  }
  *{box-sizing:border-box;margin:0;padding:0}
  html,body{width:831px;height:1200px;overflow:hidden}
  body{background:var(--stage);position:relative;font-family:"Saira",sans-serif;color:var(--ink)}

  .flyer{position:absolute;left:94px;width:644px;height:498px;overflow:hidden;
    background:linear-gradient(180deg,#ececec 0%,#ffffff 22%,#ffffff 100%)}
  .flyer--bookkeeping{top:90px}
  .flyer--payroll{top:612px}
  .flyer__waves{position:absolute;inset:0;width:644px;height:498px}

  .headline{position:absolute;font-family:"Saira Semi Condensed",sans-serif;line-height:.9}
  .headline__light{display:block;color:var(--blue);font-family:"Saira",sans-serif;font-weight:200;letter-spacing:-.5px}
  .headline__bold{display:block;color:var(--orange);font-weight:800;letter-spacing:.5px}

  .flyer--bookkeeping .headline{left:50px;top:34px}
  .flyer--bookkeeping .headline__light{font-size:40px}
  .flyer--bookkeeping .headline__bold{font-size:78px;margin-top:2px}

  .brand{position:absolute;display:flex;align-items:center;gap:8px;
    font-family:"Saira Semi Condensed",sans-serif;font-weight:700;color:var(--blue)}
  .brand__dot{width:16px;height:16px;border-radius:50%;background:var(--orange);flex:none}
  .flyer--bookkeeping .brand{left:440px;top:70px;font-size:25px}
  .flyer--payroll .brand{left:400px;top:110px;font-size:30px}

  /* pricing table */
  .pricing{position:absolute;left:38px;top:144px;width:568px;border-collapse:collapse;
    table-layout:fixed;font-family:"Saira",sans-serif;font-weight:300;font-size:12px}
  .pricing col.service{width:178px}
  .pricing td,.pricing th{border:1px solid var(--rule);text-align:center;vertical-align:middle;
    background:linear-gradient(90deg,#ffffff 0%,#ffffff 55%,#e4e5e7 100%);line-height:1.1}
  .pricing .services-head{background:linear-gradient(180deg,var(--blue) 0%,var(--blue-deep) 100%);
    color:var(--white);font-family:"Saira Semi Condensed",sans-serif;font-weight:800;font-size:24px;
    text-align:left;padding-left:30px;letter-spacing:.5px}
  .pricing .tier{background:var(--orange);color:var(--white);font-family:"Saira Semi Condensed",sans-serif;
    font-weight:700;font-size:9.5px;height:19px;letter-spacing:.4px}
  .pricing .price{background:linear-gradient(180deg,var(--blue) 0%,var(--blue-deep) 100%);color:var(--white);
    font-family:"Saira Semi Condensed",sans-serif;font-weight:800;font-size:17px;height:21px}
  .pricing .label{text-align:right;padding-right:10px;background:#fff}
  .pricing .label small{display:block;color:var(--muted);font-size:8.5px}
  .pricing .accent{color:var(--orange);font-weight:400}
  .pricing .none{color:var(--orange);font-weight:400;font-size:13px}
  .tick{display:block;margin:0 auto;width:16px;height:12px}
  .pricing tr.r1 td{height:39px}
  .pricing tr.r2 td{height:33px}
  .pricing tr.r3 td,.pricing tr.r4 td,.pricing tr.r5 td,.pricing tr.r6 td,.pricing tr.r7 td{height:33px}
  .pricing tr.r8 td{height:33px}

  .footer{position:absolute;left:0;right:0;top:460px;text-align:center;color:var(--white);
    font-family:"Saira Semi Condensed",sans-serif;font-weight:700;font-size:13.5px;letter-spacing:.1px}
  .footer span{margin:0 6px}

  /* payroll flyer */
  .flyer--payroll .headline{left:42px;top:44px}
  .flyer--payroll .headline__light{font-size:58px;line-height:.95}
  .flyer--payroll .headline__bold{font-size:72px;line-height:.78;margin-top:4px}

  .offer{position:absolute;left:0;right:0;text-align:center;color:var(--white);
    font-family:"Saira Semi Condensed",sans-serif;font-weight:800}
  .offer__line{display:block;font-size:31px;line-height:40px}
  .offer__line--big{font-size:46px;line-height:48px;letter-spacing:-.5px}
  .flyer--payroll .offer{top:274px}

  .terms{position:absolute;left:42px;top:409px;width:560px;height:40px}
  .terms__shape{position:absolute;inset:0;width:560px;height:40px}
  .terms__text{position:absolute;inset:0;display:flex;flex-direction:column;justify-content:center;align-items:center;
    color:var(--white);font-family:"Saira Semi Condensed",sans-serif;font-weight:700;font-size:8.6px;line-height:1.35}
  .terms__text em{font-style:normal;color:var(--orange)}
  .flyer--payroll .footer{top:459px}
</style>
</head>
<body>

<svg width="0" height="0" style="position:absolute">
  <defs>
    <symbol id="tick" viewBox="0 0 16 12">
      <path d="M1.5 6.5 L6 10.5 L14.5 1.5" fill="none" stroke="#e87722" stroke-width="2" stroke-linecap="round" stroke-linejoin="round"/>
    </symbol>
  </defs>
</svg>

<!-- Bookkeeping pricing flyer -->
<section class="flyer flyer--bookkeeping">
  <svg class="flyer__waves" viewBox="0 0 644 498" aria-hidden="true">
    <path d="M400 226 Q540 208 644 206 L644 246 Q520 244 400 236 Z" fill="var(--orange-deep)"/>
    <path d="M0 214 Q220 262 644 246 L644 498 L0 498 Z" fill="var(--blue)"/>
    <path d="M0 300 Q260 268 644 300 L644 498 L0 498 Z" fill="var(--orange)"/>
    <path d="M0 302 Q260 272 644 296 L644 304 Q260 280 0 308 Z" fill="var(--orange-deep)"/>
  </svg>

  <h1 class="headline">
    <span class="headline__light">BOOKKEEPING</span>
    <span class="headline__bold">PRICING</span>
  </h1>

  <div class="brand"><span class="brand__dot"></span>Northfield Ridge</div>

  <table class="pricing">
    <colgroup><col class="service"><col><col><col><col></colgroup>
    <thead>
      <tr>
        <th class="services-head" rowspan="2">SERVICES</th>
        <th class="tier">PREMIUM</th><th class="tier">ENTREPRENEUR</th><th class="tier">GROWTH</th><th class="tier">START UP</th>
      </tr>
      <tr>
        <th class="price">$999</th><th class="price">$599</th><th class="price">$299</th><th class="price">$149</th>
      </tr>
    </thead>
    <tbody>
      <tr class="r1"><td class="label">EMPLOYEES</td><td>AROUND<br>10+</td><td>AROUND<br>5-9</td><td>AROUND<br>2-5</td><td>AROUND<br>1-2</td></tr>
      <tr class="r2"><td class="label">TRANSACTIONS / MONTH</td><td>UP TO<br>250</td><td>UP TO<br>150</td><td>UP TO<br>75</td><td>UP TO<br>50</td></tr>
      <tr class="r3"><td class="label">BOOKKEEPING</td>
        <td class="accent"><svg class="tick"><use href="#tick"/></svg>WEEKLY</td>
        <td class="accent"><svg class="tick"><use href="#tick"/></svg>WEEKLY</td>
        <td class="accent"><svg class="tick"><use href="#tick"/></svg>MONTHLY</td>
        <td class="accent"><svg class="tick"><use href="#tick"/></svg>QUARTERLY</td></tr>
      <tr class="r4"><td class="label">FINANCIAL REPORTS &amp; REVIEW</td>
        <td class="accent"><svg class="tick"><use href="#tick"/></svg>MONTHLY</td>
        <td class="accent"><svg class="tick"><use href="#tick"/></svg>MONTHLY</td>
        <td class="accent"><svg class="tick"><use href="#tick"/></svg>MONTHLY</td>
        <td class="accent"><svg class="tick"><use href="#tick"/></svg>QUARTERLY</td></tr>
      <tr class="r5"><td class="label">SUPPORT<small>(PHONE AND CHAT)</small></td>
        <td><svg class="tick"><use href="#tick"/></svg></td><td><svg class="tick"><use href="#tick"/></svg></td>
        <td><svg class="tick"><use href="#tick"/></svg></td><td><svg class="tick"><use href="#tick"/></svg></td></tr>
      <tr class="r6"><td class="label">ONLINE COLLABORATION PORTAL<small>(SHARED DRIVE)</small></td>
        <td><svg class="tick"><use href="#tick"/></svg></td><td><svg class="tick"><use href="#tick"/></svg></td>
        <td><svg class="tick"><use href="#tick"/></svg></td><td><svg class="tick"><use href="#tick"/></svg></td></tr>
      <tr class="r7"><td class="label">BUSINESS TAX RETURN</td>
        <td><svg class="tick"><use href="#tick"/></svg></td><td><svg class="tick"><use href="#tick"/></svg></td>
        <td>$799</td><td>$599</td></tr>
      <tr class="r8"><td class="label">BILL PAY<small>(WITH APPROVAL PROCESS)</small></td>
        <td class="accent"><svg class="tick"><use href="#tick"/></svg>$5 / PAYMENT</td>
        <td class="none">x</td><td class="none">x</td><td class="none">x</td></tr>
    </tbody>
  </table>

  <p class="footer">1280 W HARBOR AVE, RIVERTON, UT 84065<span>•</span>555-014-2290<span>•</span>NORTHFIELDRIDGE.COM</p>
</section>

<!-- Payroll pricing flyer -->
<section class="flyer flyer--payroll">
  <svg class="flyer__waves" viewBox="0 0 644 498" aria-hidden="true">
    <path d="M0 212 Q300 168 644 214 L644 498 L0 498 Z" fill="var(--blue)"/>
    <path d="M90 252 Q380 196 644 226 L644 262 Q380 226 90 262 Z" fill="var(--orange-deep)"/>
    <path d="M0 282 Q320 226 644 296 L644 498 L0 498 Z" fill="var(--orange)"/>
  </svg>

  <h1 class="headline">
    <span class="headline__light">SIMPLIFIED</span>
    <span class="headline__bold">PAYROLL</span>
    <span class="headline__bold">PRICING</span>
  </h1>

  <div class="brand"><span class="brand__dot"></span>Northfield Ridge</div>

  <p class="offer">
    <span class="offer__line">$25 PER PAYROLL</span>
    <span class="offer__line">+$5 PER EMPLOYEE</span>
    <span class="offer__line offer__line--big">NO SET UP FEES!</span>
  </p>

  <div class="terms">
    <svg class="terms__shape" viewBox="0 0 560 40" aria-hidden="true">
      <path d="M12 0 L560 0 L548 40 L0 40 Z" fill="var(--charcoal)"/>
    </svg>
    <p class="terms__text">
      <span>DIRECT DEPOSIT ONLY, ADD $20 PER PAYROLL IF YOU ELECT TO HAVE PAPER CHECKS SHIPPED TO YOU.</span>
      <span>MINIMUM CHARGE OF TWO PAYROLLS PER MONTH. <em>COST PER EMPLOYEE DROPS TO $4 AFTER 20 EMPLOYEES.</em></span>
    </p>
  </div>

  <p class="footer">1280 W HARBOR AVE, RIVERTON, UT 84065<span>•</span>555-014-2290<span>•</span>NORTHFIELDRIDGE.COM</p>
</section>

</body>
</html>
```